Business Card Design

I would like a new business card design for an accounting firm that specializes in resolving clients tax problems. I want the card to give the impression that we are not your typical stodgy accounting firm, but at the same time we will get the job done.
Industry/Entity Type
Business
Contact Information for Business Card
Dorian T Welsby
Certified Public Accountant
38-27 52nd Street
Sunnyside, NY 11287
Tel: (718) 555-0142
Fax: (888) 555-0199
e-mail: dtwthecpa@ledgerpost.com
website: harborfilingreliefexperts.com

```html
<!DOCTYPE html>
<html lang="en">
<head>
<meta charset="utf-8">
<title>Dorian T Welsby — Business Card</title>
<link href="https://fonts.googleapis.com/css2?family=Open+Sans:wght@400;600;700&display=swap" rel="stylesheet">
<style>
  :root {
    --backdrop: #e8e5e0;
    --card: #fbfbfb;
    --brand-blue: #1f4f9c;
    --brand-blue-deep: #163c7a;
    --ink: #3a3d42;
    --ink-soft: #5c6068;
    --rule: #8ea4c8;
  }
  * { box-sizing: border-box; margin: 0; padding: 0; }
  html, body {
    width: 1200px; height: 1023px; overflow: hidden;
    background: var(--backdrop);
    font-family: "Open Sans", Arial, sans-serif;
  }
  .stage {
    width: 1200px; height: 1023px;
    display: flex; align-items: center; justify-content: center;
  }
  .card {
    position: relative;
    width: 1000px; height: 572px;
    background: var(--card);
    border-radius: 6px;
    box-shadow: 0 18px 40px rgba(0,0,0,.18), 0 2px 6px rgba(0,0,0,.12);
    overflow: hidden;
  }
  .edge-tab {
    position: absolute;
    width: 22px;
    background: linear-gradient(90deg, var(--brand-blue-deep), var(--brand-blue));
  }
  .edge-tab--left { left: 0; bottom: 0; height: 270px; border-top-right-radius: 14px; }
  .edge-tab--right { right: 0; top: 0; height: 270px; border-bottom-left-radius: 14px; }
  .divider {
    position: absolute; left: 500px; top: 124px;
    width: 1px; height: 324px; background: var(--rule);
  }
  .contact {
    position: absolute; left: 72px; top: 150px;
    color: var(--ink);
  }
  .contact__name {
    font-size: 30px; font-weight: 700; color: var(--brand-blue);
    line-height: 1.15;
  }
  .contact__title {
    font-size: 21px; font-weight: 400; color: var(--ink-soft);
    margin-bottom: 22px;
  }
  .contact__list { list-style: none; }
  .contact__item {
    display: flex; align-items: center; gap: 14px;
    font-size: 20px; line-height: 34px;
  }
  .icon {
    width: 22px; height: 22px; border-radius: 4px;
    background: var(--brand-blue);
    flex: none;
  }
  .contact__address {
    font-style: normal; font-size: 20px; line-height: 30px;
    margin-top: 18px;
  }
  .firm-name {
    position: absolute; left: 500px; right: 0; top: 230px;
    display: flex; align-items: center; justify-content: center; gap: 16px;
  }
  .firm-name__mark {
    width: 22px; height: 22px; background: var(--brand-blue);
  }
  .firm-name__text {
    font-size: 36px; font-weight: 700; color: var(--brand-blue);
    letter-spacing: 2px;
  }
</style>
</head>
<body>
<main class="stage">
  <article class="card">
    <div class="edge-tab edge-tab--left"></div>
    <div class="edge-tab edge-tab--right"></div>
    <div class="divider"></div>

    <section class="contact">
      <h1 class="contact__name">Dorian T Welsby</h1>
      <p class="contact__title">Certified Public Accountant</p>
      <ul class="contact__list">
        <li class="contact__item">
          <svg class="icon" viewBox="0 0 22 22" aria-hidden="true"><rect width="22" height="22" rx="4" fill="#1f4f9c"/><path d="M7 5c1 0 2 2.5 2 3s-1 1-1 1.6c.5 1.6 2 3 3.4 3.4.6 0 1-1 1.6-1s3 1 3 2-1.2 2.5-2.5 2.5C9 16.5 5.5 13 5.5 8 5.5 6.2 6 5 7 5z" fill="#fff"/></svg>
          <span>(718) 555-0142</span>
        </li>
        <li class="contact__item">
          <svg class="icon" viewBox="0 0 22 22" aria-hidden="true"><rect width="22" height="22" rx="4" fill="#1f4f9c"/><rect x="7" y="4.5" width="8" height="4" fill="#fff"/><rect x="4.5" y="9" width="13" height="6" rx="1" fill="#fff"/><rect x="7" y="13" width="8" height="4.5" fill="#fff" stroke="#1f4f9c" stroke-width="1"/></svg>
          <span>(888) 555-0199</span>
        </li>
        <li class="contact__item">
          <svg class="icon" viewBox="0 0 22 22" aria-hidden="true"><rect width="22" height="22" rx="4" fill="#1f4f9c"/><rect x="4.5" y="6.5" width="13" height="9" fill="#fff"/><path d="M4.5 6.5 11 12l6.5-5.5" fill="none" stroke="#1f4f9c" stroke-width="1.3"/></svg>
          <span>dtwthecpa@ledgerpost.com</span>
        </li>
        <li class="contact__item">
          <svg class="icon" viewBox="0 0 22 22" aria-hidden="true"><rect width="22" height="22" rx="4" fill="#1f4f9c"/><circle cx="11" cy="11" r="6" fill="none" stroke="#fff" stroke-width="1.4"/><ellipse cx="11" cy="11" rx="2.6" ry="6" fill="none" stroke="#fff" stroke-width="1.2"/><path d="M5 11h12" stroke="#fff" stroke-width="1.2"/></svg>
          <span>www.dorianwelsbycpa.com</span>
        </li>
      </ul>
      <address class="contact__address">
        38-27 52nd Street<br>
        Sunnyside, NY 11287
      </address>
    </section>

    <div class="firm-name">
      <span class="firm-name__mark"></span>
      <span class="firm-name__text">DORIAN T. WELSBY</span>
    </div>
  </article>
</main>
</body>
</html>
```